Label and logo design for an all natural organic skincare product

We need a label design for a new company in the natural beauty space. The company is called "Vessa Kell". "Vessa" refers to the olive tree. "Kell" symbolizes the wren bird. The company name represents purity, nature, and freedom.

Our first product is tamanu oil - a 100% pure, organic, unrefined, cold pressed oil that is be used to improve various skin conditions (acne, eczema, scars, anti-aging) hair, and nails. Tamanu oil is a wonderful skin care healing agent that fades scars, rejuvenates skin cells, and is a powerful natural anti-aging product.

We currently do not have a company logo. We would like the logo and label to be designed together for a coordinated, well thought out, look.

We are looking for a label and logo that convey a high end quality product. We use premium quality all natural ingredients only.

Label size is 10.2cm (wide) x 4.5cm (height). The label wraps around a small amber colored glass bottle with a dropper similar to the images attached. The bottle holds 1oz (30ml) of oil.

Label will contain:
- Company logo
- Product name - "100% Pure Organic Tamanu Oil"
- Quantity - "1 fl oz / 30 ml"
- Ingredients - "100% pure virgin organic cold pressed tamanu oil (calophyllum inophyllum)
- Product Usage - "Dab a few drops of Vessa Kell tamanu oil into your hands and rub the oil into your skin or hair 1 - 3 times a day."
- UPC barcode - will provide later
- Company info:
"Vessa Kell
Linden Ford, TN
www.vessakell.example"
- Warning - "For external use only. Do not use if you have allergies to nuts of any kind. Keep out of reach of children."

We've attached a couple images of labels that we like. In general, we prefer a modern, minimalistic, pure look but we are open to your ideas and creativity.

Colors we like: blue-green (think torquoise or tiffany blue), green, grey, white.

If you have any questions, about the design please let me know. The winning designer will be required to do a few additional tweaks to finalize the product. Thank you for your time and happy designing!

```html
<!DOCTYPE html>
<html lang="en">
<head>
<meta charset="utf-8">
<title>Vessa Kell Tamanu Oil Label</title>
<link href="https://fonts.googleapis.com/css2?family=Cinzel:wght@400;600;700&display=swap" rel="stylesheet">
<style>
  :root {
    --olive: #c8bf3c;
    --forest: #62754f;
    --forest-text: #5d6e4a;
    --white: #ffffff;
    --paper: #ffffff;
    --pattern-tint: #f3f0d2;
    --pattern-edge: #ece8bf;
    --hairline: #eeeacb;
  }
  * { margin: 0; padding: 0; box-sizing: border-box; }
  html, body { width: 1200px; height: 1000px; overflow: hidden; background: var(--paper); }
  body { position: relative; font-family: "Cinzel", serif; }

  .label { position: absolute; left: 151px; top: 302px; width: 899px; height: 396px; }

  .panel { position: absolute; top: 0; height: 396px; }
  .panel--ingredients { left: 0; width: 246px; background: var(--olive); color: var(--white); }
  .panel--front { left: 246px; width: 407px; background: var(--white); border-top: 1px solid var(--hairline); border-bottom: 1px solid var(--hairline); }
  .panel--warnings { left: 653px; width: 246px; background: var(--olive); color: var(--forest-text); }

  .panel-copy { position: absolute; font-weight: 700; font-size: 17px; line-height: 24px; letter-spacing: 0.2px; }
  .panel--ingredients .panel-copy { left: 17px; top: 21px; }
  .panel--warnings .panel-copy { left: 30px; top: 35px; }
  .panel-copy p + p { margin-top: 23px; }

  .company-info { position: absolute; left: 0; width: 246px; top: 322px; text-align: center; font-weight: 700; font-size: 15px; line-height: 19px; color: var(--white); }

  .botanical-pattern {
    position: absolute; inset: 6px;
    background: radial-gradient(ellipse at 50% 50%, var(--white) 30%, var(--pattern-tint) 75%, var(--pattern-edge) 100%);
    opacity: 0.9;
  }

  .brand-name { position: absolute; left: 0; top: 44px; width: 407px; text-align: center; font-size: 31px; font-weight: 400; color: var(--forest); letter-spacing: 3px; }

  .product-plate { position: absolute; left: 21px; top: 156px; width: 364px; height: 134px; background: var(--forest); border-radius: 20px; }
  .product-plate-inner { position: absolute; left: 12px; top: 12px; right: 12px; bottom: 12px; border: 2.5px solid var(--white); border-radius: 15px; text-align: center; color: var(--white); }
  .product-tagline { margin-top: 20px; font-size: 21px; letter-spacing: 3px; font-weight: 400; }
  .product-name { margin-top: -2px; font-size: 44px; font-weight: 600; letter-spacing: 1px; line-height: 50px; }

  .quantity { position: absolute; left: 140px; top: 341px; width: 125px; height: 30px; border-radius: 7px; background: var(--olive); color: var(--white); font-weight: 700; font-size: 15px; line-height: 30px; text-align: center; }
</style>
</head>
<body>
  <div class="label">
    <section class="panel panel--ingredients">
      <div class="panel-copy">
        <p>100% pure virgin<br>organic cold<br>pressed tamanu oil<br>(calophyllum<br>inophyllum).</p>
        <p>Dab a few drops of<br>Vessa Kell tamanu<br>oil into your<br>hands and rub the<br>oil into your skin<br>or hair 1 - 3 times a<br>day.</p>
      </div>
    </section>

    <section class="panel panel--front">
      <div class="botanical-pattern" role="img" aria-label="Fine line botanical pattern of tamanu fruit and leaves"></div>
      <div class="brand-name">Vessa Kell</div>
      <div class="product-plate">
        <div class="product-plate-inner">
          <div class="product-tagline">100% Pure Organic</div>
          <div class="product-name">Tamanu Oil</div>
        </div>
      </div>
      <div class="quantity">fl oz / 30 ml</div>
    </section>

    <section class="panel panel--warnings">
      <div class="panel-copy">
        <p>For external use<br>only.</p>
        <p>Do not use if you<br>have allergies<br>to nuts of any<br>kind.</p>
        <p>Keep out of reach<br>of children.</p>
      </div>
      <div class="company-info">Vessa Kell<br>Linden Ford, TN<br>www.vessakell.example</div>
    </section>
  </div>
</body>
</html>
```